Merrivale construction website for a high end luxury custom home builder

I need a website designed for a high end luxury custom home builder. I would like the website to host a number activities. A blog/vlog on the page where I can post about the projects being built how to's what to look out for during the build, A designated testimonial page but also having testimonials posted on the other pages like the gallery linked to the photos of the completed projects. a gallery page, an about us page, services page that demonstrate what we do and what we are capable of, and hopefully when I start winning awards, and awards page.
Home page
about us page
services page
gallery
testimonial
awards page but I my need to add that later.
I already have the domain name for the website. www.merrivaleconstruction.com.au
I recently completed a sketch hive page for my logo and will post the logo documents below.

Target Market(s)

I'd like to target professions with cash enough to build a house. I would like peolpe to understand that they are buy a price when they are getting quote to build there house. It seems like people just look for the cheapest price and end up with an inferior product. Where as people need to understand that a builder with the high price ( not astronomically higher 15-20% higher) are the ones with correct systems in place, a bide by correct OHS and use proper and correct product. If that can be conveyed through the website somehow, without saying it directly, it would be awesome.

Font styles to use
Sans Serif

Requirements
Must have
• I would like the testimonials to have a designated page (mentioned in the brief) but I would like the testimonials to be linked to the gallery page and when the picture are open of completed job the relevant testimonials would pop up near the pictures.

Nice to have
• I would like peolpe to understand that they are buy a price when they are getting quote to build there house. It seems like people just look for the cheapest price and end up with an inferior product. Where as people need to understand that a builder with the high price ( not astronomically higher 15-20% higher) are the ones with correct systems in place, a bide by correct OHS and use proper and correct product. If that can be conveyed through the website somehow, without saying it directly, it would be awesome.

```html
<!DOCTYPE html>
<html lang="en">
<head>
<meta charset="utf-8">
<title>Merrivale Construction – High End Luxury Custom Home Builder</title>
<link href="https://fonts.googleapis.com/css2?family=Cinzel:wght@700&family=Open+Sans:ital,wght@0,400;0,600;0,700;1,600&display=swap" rel="stylesheet">
<style>
:root{
  --blue:#1565c8;
  --blue-btn:#196cb9;
  --ink:#2b2b2b;
  --body:#7a7a7a;
  --footer:#4a4a4c;
  --white:#ffffff;
}
*{margin:0;padding:0;box-sizing:border-box}
html,body{width:1200px;height:3595px;overflow:hidden}
body{position:relative;font-family:"Open Sans",sans-serif;color:var(--ink);background:var(--white)}
a{color:inherit;text-decoration:none}
.photo{position:absolute}

/* brand */
.brand{position:absolute;color:var(--white);font-family:"Open Sans",sans-serif;font-weight:700;line-height:1;display:flex;align-items:center;gap:12px}
.brand-mark{width:44px;height:44px;border-radius:50%;background:var(--white);flex:none}
.brand-name{font-size:28px;letter-spacing:1px}
.brand-name small{display:block;font-size:13px;letter-spacing:5px;margin-top:4px}

/* hero */
.hero{position:absolute;left:0;top:0;width:1200px;height:643px}
.hero .photo{inset:0;background:linear-gradient(180deg,#1c4fc0 0%,#2a55a8 28%,#6a5440 55%,#8a5a30 75%,#3d2c20 100%)}
.nav{position:absolute;top:44px;left:463px;display:flex;gap:23px;color:var(--white);font-size:18px}
.nav .active{text-decoration:underline;text-underline-offset:4px}
.nav-contact{position:absolute;left:946px;top:35px;width:134px;height:50px;border:2px solid var(--white);border-radius:25px;color:var(--white);font-size:16px;font-weight:600;display:flex;align-items:center;justify-content:center;text-transform:uppercase}
.hero-title{position:absolute;top:140px;width:100%;text-align:center;font-family:"Cinzel",serif;font-weight:700;font-size:60px;color:var(--white);text-shadow:0 2px 8px rgba(0,0,0,.35);white-space:nowrap}
.hero-sub{position:absolute;top:224px;width:100%;text-align:center;font-size:31px;font-weight:600;color:var(--white);text-shadow:0 2px 6px rgba(0,0,0,.4)}
.btn-white{position:absolute;width:234px;height:68px;border-radius:34px;background:var(--white);color:#222;font-size:22px;font-weight:600;display:flex;align-items:center;justify-content:center;text-transform:uppercase}
.dots{position:absolute;top:592px;left:565px;display:flex;gap:6px}
.dots span{width:13px;height:13px;border-radius:50%;border:2px solid var(--white)}
.dots span.on{background:var(--white)}

/* welcome */
.section-title{font-family:"Cinzel",serif;font-weight:700;color:var(--ink);text-transform:uppercase}
.welcome-copy{position:absolute;left:110px;top:714px;width:480px}
.welcome-title{font-size:33px;line-height:49px;white-space:nowrap}
.welcome-text{margin-top:24px;padding-left:2px;font-size:16px;line-height:31px;color:var(--body)}
.welcome-text p+p{margin-top:31px}
.btn-blue{margin:30px 0 0 2px;width:169px;height:56px;border-radius:28px;background:var(--blue-btn);color:var(--white);font-size:16px;font-weight:700;display:flex;align-items:center;justify-content:center}
.video{position:absolute;left:629px;top:725px;width:459px;height:292px;background:linear-gradient(135deg,#8a96a8,#c9ccc8 45%,#d6c55a 70%,#6a7fa0)}
.play{position:absolute;left:199px;top:116px;width:62px;height:62px;border-radius:50%;background:#111;display:flex;align-items:center;justify-content:center}

/* testimonial */
.testimonial{position:absolute;left:0;top:1205px;width:1200px;height:493px;overflow:hidden}
.testimonial .photo{inset:0;background:linear-gradient(180deg,#9fb7d8 0%,#cfd3dc 40%,#8a8c94 70%,#6d5a48 100%)}
.testimonial .curve{position:absolute;inset:0}
.quote-mark{position:absolute;left:572px;top:-12px;font-family:Georgia,serif;font-size:140px;line-height:1;color:var(--white);font-weight:700}
.quote-text{position:absolute;left:587px;top:90px;width:510px;font-size:20px;line-height:33.5px;font-style:italic;font-weight:600;color:var(--white)}
.quote-author{position:absolute;right:114px;top:275px;font-size:22px;color:var(--white)}
.quote-author b{font-weight:600}
.quote-arrows{position:absolute;left:1034px;top:350px}

/* gallery */
.gallery-title{position:absolute;top:1760px;width:100%;text-align:center;font-size:38px}
.gallery-item{position:absolute;top:1848px;width:318px;height:331px}
.g1{left:112px;background:linear-gradient(135deg,#e8e8e8,#bfc0c2 60%,#8f9092)}
.g2{left:441px;background:linear-gradient(180deg,#6fc0dd 0%,#5a5a58 45%,#3e3a36 100%)}
.g3{left:770px;background:linear-gradient(180deg,#d9d9d9 0%,#4a4c50 40%,#9a6c45 100%)}
.gallery-arrow{position:absolute;top:1994px}

/* cta */
.cta{position:absolute;left:0;top:2260px;width:1200px;height:387px}
.cta .photo{inset:0;background:linear-gradient(180deg,#3a4557 0%,#5a4a42 45%,#3f4a34 80%,#35452a 100%)}
.cta-title{position:absolute;top:70px;width:100%;text-align:center;font-family:"Cinzel",serif;font-weight:700;font-size:40px;color:var(--white)}
.cta-text{position:absolute;top:135px;left:240px;width:720px;text-align:center;font-size:21px;line-height:38px;color:var(--white)}

/* blog */
.blog-title{position:absolute;top:2715px;width:100%;text-align:center;font-size:38px}
.post{position:absolute;top:2803px;width:303px}
.post-img{height:230px}
.p1 .post-img{background:linear-gradient(135deg,#f2f2f2,#c9c5c0 55%,#4a3a34)}
.p2 .post-img{background:linear-gradient(135deg,#2e2e2e,#5a5550 55%,#c98a4a)}
.p3 .post-img{background:linear-gradient(180deg,#8fc0ea 0%,#b06a45 45%,#9a9a98 100%)}
.post h3{margin-top:25px;font-size:22px;font-weight:400;color:var(--ink)}
.post-meta{margin-top:10px;font-size:14px;color:#555;display:flex;align-items:center;gap:6px}
.post-meta svg{flex:none}
.post p{margin-top:16px;font-size:14px;line-height:27px;color:var(--body)}
.post .more{display:block;margin-top:15px;font-size:15px;font-weight:700;color:var(--blue-btn)}

/* footer */
.footer{position:absolute;left:0;top:3326px;width:1200px;height:269px;background:var(--footer);color:var(--white)}
.footer .brand{left:110px;top:40px}
.socials{position:absolute;left:110px;top:152px;display:flex;gap:9px}
.socials span{width:42px;height:42px;border:2px solid var(--white);border-radius:50%}
.copyright{position:absolute;left:110px;top:214px;font-size:15px}
.footer-links{position:absolute;top:65px;list-style:none;font-size:14.5px;line-height:32.5px}
.fl1{left:499px}.fl2{left:628px}
.contact{position:absolute;left:862px;top:65px;font-size:14.5px;list-style:none}
.contact li{display:flex;gap:9px;align-items:flex-start;line-height:25px}
.contact li+li{margin-top:22px}
.contact svg{margin-top:5px;flex:none}
</style>
</head>
<body>

<header class="hero">
  <div class="photo" role="img" aria-label="Luxury modern home at dusk with open bi-fold doors and warmly lit interior"></div>
  <div class="brand" style="left:112px;top:24px">
    <span class="brand-mark"></span>
    <span class="brand-name">MERRIVALE<small>CONSTRUCTION</small></span>
  </div>
  <nav class="nav">
    <a class="active" href="#">Home</a>
    <a href="#">Services</a>
    <a href="#">Gallery</a>
    <a href="#">Testimonial</a>
    <a href="#">Awards</a>
  </nav>
  <a class="nav-contact" href="#">Contact Us</a>
  <h1 class="hero-title">MERRIVALE CONSTRUCTION</h1>
  <p class="hero-sub">High End Luxury Custom Home Builder</p>
  <a class="btn-white" href="#" style="left:483px;top:297px">Get a Quote</a>
  <div class="dots"><span class="on"></span><span></span><span></span><span></span></div>
</header>

<section class="welcome">
  <div class="welcome-copy">
    <h2 class="section-title welcome-title">Welcome to Merrivale<br>Construction</h2>
    <div class="welcome-text">
      <p>Nemo enim ipsam voluptatem quia voluptas sit aspernatur aut odit aut fugit, sed quia consequunt.</p>
      <p>Sur magni dolores eos qui ratione voluptatem sequi nesciunue porro quisquam est, qui dolorem ipsum quia dolor sit ametcon sectetur, adipisci velit, sed quia non numquam eius modi temp ora incidunt ut labore et dolore mag.</p>
    </div>
    <a class="btn-blue" href="#">READ MORE</a>
  </div>
  <div class="video" role="img" aria-label="Video thumbnail: builders in hard hats reviewing house plans">
    <span class="play"><svg width="24" height="26" viewBox="0 0 24 26"><path d="M3 1 L23 13 L3 25 Z" fill="#fff"/></svg></span>
  </div>
</section>

<section class="testimonial">
  <div class="photo" role="img" aria-label="Completed two-storey luxury home exterior at twilight"></div>
  <svg class="curve" width="1200" height="493" viewBox="0 0 1200 493" aria-hidden="true">
    <path d="M380 0 Q300 250 370 493 L1200 493 L1200 0 Z" fill="#1565c8" fill-opacity=".82"/>
  </svg>
  <div class="quote-mark">&ldquo;</div>
  <p class="quote-text">Nam libero tempore, cum soluta nobis est eligendioptio cumque nihil impedit quo miid quod maxime placeatac ere possimus, omnis volup tas assumenda est, omnisdo lor repell endu poribus autem qui sdam et aut officiis debitis aut rerum neces.</p>
  <p class="quote-author"><b>- Sam Whitford</b>&nbsp; Home Owner</p>
  <svg class="quote-arrows" width="52" height="24" viewBox="0 0 52 24" aria-label="Previous and next testimonial">
    <circle cx="12" cy="12" r="11" fill="#fff"/>
    <path d="M14.5 6.5 L8.5 12 L14.5 17.5" stroke="#222" stroke-width="2.6" fill="none" stroke-linecap="round" stroke-linejoin="round"/>
    <circle cx="40" cy="12" r="11" fill="#fff"/>
    <path d="M37.5 6.5 L43.5 12 L37.5 17.5" stroke="#222" stroke-width="2.6" fill="none" stroke-linecap="round" stroke-linejoin="round"/>
  </svg>
</section>

<section class="gallery">
  <h2 class="section-title gallery-title">Gallery</h2>
  <svg class="gallery-arrow" style="left:44px" width="18" height="32" viewBox="0 0 18 32"><path d="M16 2 L3 16 L16 30" stroke="#999" stroke-width="3" fill="none"/></svg>
  <div class="gallery-item g1" role="img" aria-label="Marble bathroom with freestanding bath and fireplace"></div>
  <div class="gallery-item g2" role="img" aria-label="Modern brick apartment building against blue sky"></div>
  <div class="gallery-item g3" role="img" aria-label="Dark grey kitchen with pendant lights and timber stools"></div>
  <svg class="gallery-arrow" style="left:1138px" width="18" height="32" viewBox="0 0 18 32"><path d="M2 2 L15 16 L2 30" stroke="#999" stroke-width="3" fill="none"/></svg>
</section>

<section class="cta">
  <div class="photo" role="img" aria-label="Luxury home with pool terrace and lawn at dusk"></div>
  <h2 class="cta-title">HIGH END LUXURY CUSTOM HOME BUILDER</h2>
  <p class="cta-text">Nam libero tempore, cum soluta nobis est eligendi optio cumque nihil impedit quo minus id quod maxime placeat facere possi.</p>
  <a class="btn-white" href="#" style="left:483px;top:241px">Get a Quote</a>
</section>

<section class="blog">
  <h2 class="section-title blog-title">Latest Blog</h2>
  <article class="post p1" style="left:112px">
    <div class="post-img" role="img" aria-label="Bright white kitchen with dark island bench"></div>
    <h3>Finibus Bonoruet Malorum</h3>
    <div class="post-meta"><svg width="12" height="12" viewBox="0 0 12 12"><rect x="0.5" y="1.5" width="11" height="10" fill="none" stroke="#1565c8"/><rect x="0.5" y="1.5" width="11" height="3" fill="#1565c8"/></svg>30/06/2020 &nbsp;|&nbsp; <svg width="11" height="12" viewBox="0 0 11 12"><circle cx="5.5" cy="3" r="3" fill="#1565c8"/><path d="M0 12 Q5.5 4 11 12 Z" fill="#1565c8"/></svg>Sam Whitford</div>
    <p>Nam libero tempore, cum soluta nobis esteli gendi optio cumque nihil impedit quo minus id quod maxime placeat.</p>
    <a class="more" href="#">READ MORE</a>
  </article>
  <article class="post p2" style="left:448px">
    <div class="post-img" role="img" aria-label="Dark modern kitchen with lit island bench"></div>
    <h3>Finibus Bonoruet Malorum</h3>
    <div class="post-meta"><svg width="12" height="12" viewBox="0 0 12 12"><rect x="0.5" y="1.5" width="11" height="10" fill="none" stroke="#1565c8"/><rect x="0.5" y="1.5" width="11" height="3" fill="#1565c8"/></svg>30/06/2020 &nbsp;|&nbsp; <svg width="11" height="12" viewBox="0 0 11 12"><circle cx="5.5" cy="3" r="3" fill="#1565c8"/><path d="M0 12 Q5.5 4 11 12 Z" fill="#1565c8"/></svg>Sam Whitford</div>
    <p>Nam libero tempore, cum soluta nobis esteli gendi optio cumque nihil impedit quo minus id quod maxime placeat.</p>
    <a class="more" href="#">READ MORE</a>
  </article>
  <article class="post p3" style="left:784px">
    <div class="post-img" role="img" aria-label="Two-storey home with timber cladding and driveway"></div>
    <h3>Finibus Bonoruet Malorum</h3>
    <div class="post-meta"><svg width="12" height="12" viewBox="0 0 12 12"><rect x="0.5" y="1.5" width="11" height="10" fill="none" stroke="#1565c8"/><rect x="0.5" y="1.5" width="11" height="3" fill="#1565c8"/></svg>30/06/2020 &nbsp;|&nbsp; <svg width="11" height="12" viewBox="0 0 11 12"><circle cx="5.5" cy="3" r="3" fill="#1565c8"/><path d="M0 12 Q5.5 4 11 12 Z" fill="#1565c8"/></svg>Sam Whitford</div>
    <p>Nam libero tempore, cum soluta nobis esteli gendi optio cumque nihil impedit quo minus id quod maxime placeat.</p>
    <a class="more" href="#">READ MORE</a>
  </article>
</section>

<footer class="footer">
  <div class="brand">
    <span class="brand-mark"></span>
    <span class="brand-name">MERRIVALE<small>CONSTRUCTION</small></span>
  </div>
  <div class="socials">
    <span aria-label="Social profile"></span><span aria-label="Social profile"></span><span aria-label="Social profile"></span><span aria-label="Social profile"></span>
  </div>
  <p class="copyright">Copyright 2020. All Rights Reserved.</p>
  <ul class="footer-links fl1">
    <li>Home</li><li>Services</li><li>Gallery</li><li>Testimonial</li><li>Awards</li>
  </ul>
  <ul class="footer-links fl2">
    <li>Terms &amp; Conditions</li><li>Disclaimer</li><li>Sitemap</li><li>Privacy Policy</li>
  </ul>
  <ul class="contact">
    <li><svg width="10" height="14" viewBox="0 0 10 14"><path d="M5 0 A5 5 0 0 1 10 5 C10 9 5 14 5 14 C5 14 0 9 0 5 A5 5 0 0 1 5 0 Z" fill="#fff"/><circle cx="5" cy="5" r="2" fill="#4a4a4c"/></svg><span>Suite 4 / 212 Harbour Road<br>WA 6021</span></li>
    <li><svg width="12" height="12" viewBox="0 0 12 12"><path d="M2 0 L4.5 0 L5.5 3 L4 4.5 Q5.5 7.5 7.5 8 L9 6.5 L12 7.5 L12 10 Q11 12 9 12 Q0 10 0 2 Q0 0 2 0 Z" fill="#fff"/></svg><span>1 800 555 0142</span></li>
    <li><svg width="14" height="11" viewBox="0 0 14 11"><rect width="14" height="11" fill="#fff"/><path d="M0 0 L7 6 L14 0" stroke="#4a4a4c" stroke-width="1.4" fill="none"/></svg><span>info@merrivaleconstruction.com</span></li>
  </ul>
</footer>

</body>
</html>
```